School Wide Powerpoint design

We are looking to have a powerpoint template created that can be used across the organization for presentation. It must be in brand (see guidelines attached)

Target Market(s)

Board meetings, prospective families, donors, school community

Colors

Designer to choose colors to be used in the design.

Requirements
Must have
• In brand (Fonts \ colors)

```html
<!DOCTYPE html>
<html lang="en">
<head>
<meta charset="utf-8">
<title>Meadowbrook School – Presentation Template</title>
<link rel="stylesheet" href="https://fonts.googleapis.com/css2?family=Libre+Baskerville:wght@400;700&family=Montserrat:wght@400;600;700&display=swap">
<style>
:root{
  --navy:#1f3a55;
  --navy-deep:#172e44;
  --gold:#e2b72c;
  --red:#e84c3d;
  --orange:#f57c1f;
  --green:#2b4f31;
  --grey:#7a7a7a;
  --grey-light:#d9d9d9;
  --ink:#555;
  --canvas:#f3f3f3;
  --serif:"Libre Baskerville", Georgia, serif;
  --sans:"Montserrat", Arial, sans-serif;
}
*{box-sizing:border-box;margin:0;padding:0}
html,body{width:1064px;height:1200px;overflow:hidden;background:var(--canvas)}
.slide{position:absolute;width:425px;height:240px;background:#fff;transform:scale(.8);transform-origin:0 0;overflow:hidden;box-shadow:0 0 0 1px #e2e2e2;font-family:var(--sans);color:var(--ink)}
.slide>svg.art{position:absolute;inset:0;width:425px;height:240px}
.abs{position:absolute}
.ttl{position:absolute;left:9px;top:10px;font:400 12px/1 var(--serif);color:var(--navy);letter-spacing:.3px}
.ttl .hl{color:var(--red)}
.logo{position:absolute;top:7px;right:6px;font:400 6px/1.05 var(--serif);color:var(--navy);text-align:right;display:flex;align-items:center;gap:3px}
.logo::before{content:"";width:6px;height:6px;border-radius:50%;background:var(--navy)}
.foot{position:absolute;left:0;right:0;bottom:0;height:10px;background:var(--navy);font:600 3.6px/10px var(--sans);color:#fff;padding:0 6px}
.foot::after{content:"";position:absolute;right:0;top:0;width:72px;height:10px;background:var(--gold);clip-path:polygon(10px 0,100% 0,100% 100%,0 100%)}
.foot .pg{position:absolute;right:8px;top:0;z-index:1;color:var(--navy)}
.p{font:400 4px/1.6 var(--sans);color:var(--ink)}
.p.c{text-align:center}
.p.j{text-align:justify}
.p.r{text-align:right}
.h{font:700 5px/1.3 var(--sans);color:var(--navy)}
.h.red{color:var(--red)}
.h.gold{color:var(--gold)}
.serif-h{font:400 9px/1.2 var(--serif);color:var(--navy)}
.cover-title{font:400 10px/1 var(--serif);color:var(--navy);letter-spacing:1px}
.bullet{display:flex;gap:5px;align-items:flex-start;margin-bottom:10px}
.bullet .mk{width:0;height:0;border-left:6px solid var(--navy);border-top:3.5px solid transparent;border-bottom:3.5px solid transparent;margin-top:2px}
.card-label{font:700 6px/1 var(--sans);color:var(--navy);text-align:center;margin:3px 0 4px}
.row-box .h{font-size:4.6px}
.num{font:700 8px/1 var(--sans);fill:#fff}
.year{font:700 10px/1 var(--sans);fill:#fff;text-anchor:middle;letter-spacing:1px}
.axis{font:400 4.5px var(--sans);fill:#444}
.tiny{font:400 3.6px var(--sans);fill:#666}
.svg-h{font:700 4.6px var(--sans);fill:var(--navy)}
.table{position:absolute;left:0;top:58px;width:425px;border-collapse:collapse;font:400 3.4px/1 var(--sans);color:#555}
.table th{background:var(--orange);color:#fff;font:700 4.6px/12px var(--serif);height:12px;border-right:1px solid #fff}
.table td{background:#e4e4e4;padding:2.2px 0 2.2px 22px;border-right:1px solid #fff}
.thanks{position:absolute;left:0;top:56px;width:175px;height:34px;background:var(--gold);clip-path:polygon(0 0,100% 0,92% 100%,0 100%);font:700 12px/34px var(--sans);color:#fff;padding-left:28px;letter-spacing:.5px}
.thanks-brand{position:absolute;left:28px;top:106px;font:400 11px/1.15 var(--serif);color:#fff}
.thanks-addr{position:absolute;left:28px;top:160px;font:400 6px/1.7 var(--serif);color:#fff}
</style>
</head>
<body>

<!-- 1 · Cover -->
<section class="slide" style="left:17px;top:16px">
  <svg class="art" viewBox="0 0 425 240">
    <defs><linearGradient id="g1" x1="0" y1="0" x2="1" y2="1"><stop offset="0" stop-color="#8d9396"/><stop offset="1" stop-color="#3f4a52"/></linearGradient></defs>
    <g role="img" aria-label="Photo of hands writing beside a laptop"><polygon points="0,0 215,0 160,240 0,240" fill="url(#g1)"/></g>
    <polygon points="198,75 206,75 167,240 159,240" fill="var(--gold)"/>
    <polygon points="425,170 425,240 395,240" fill="var(--navy)"/>
    <polygon points="425,170 425,205 413,185" fill="var(--red)"/>
  </svg>
  <div class="logo">MEADOWBROOK SCHOOL<br>at LINDEN</div>
  <div class="abs" style="left:233px;top:60px;width:170px">
    <div class="cover-title">OUR TRAINING COURSES</div>
    <p class="p" style="margin-top:4px">Lorem ipsum dolor sit amet, consectetur adipiscing elit, sed do eiusmod tempor incididunt ut labore magna aliqua.</p>
  </div>
  <div class="abs" style="left:216px;top:103px;width:200px">
    <div class="bullet"><span class="mk"></span><div><div class="serif-h">Bullet Point text here</div><p class="p">Lorem ipsum dolor sit amet, consectetur adipiscing elit, sed do eiusmod tempor incididunt ut labor aliqua.</p></div></div>
    <div class="bullet"><span class="mk"></span><div><div class="serif-h">Bullet Point text here</div><p class="p">Lorem ipsum dolor sit amet, consectetur adipiscing elit, sed do eiusmod tempor incididunt ut labor aliqua.</p></div></div>
    <div class="bullet"><span class="mk"></span><div><div class="serif-h">Bullet Point text here</div><p class="p">Lorem ipsum dolor sit amet, consectetur adipiscing elit, sed do eiusmod tempor incididunt ut labor aliqua.</p></div></div>
  </div>
</section>

<!-- 2 · Icon process -->
<section class="slide" style="left:364px;top:16px">
  <svg class="art" viewBox="0 0 425 240">
    <rect x="38" y="58" width="97" height="142" rx="12" fill="none" stroke="var(--gold)" stroke-width="3"/>
    <rect x="168" y="58" width="98" height="142" rx="12" fill="none" stroke="var(--navy)" stroke-width="3"/>
    <rect x="300" y="58" width="98" height="142" rx="12" fill="none" stroke="var(--navy)" stroke-width="3"/>
    <path d="M135,92 H152 V70 Q152,58 164,58" fill="none" stroke="var(--gold)" stroke-width="3"/>
    <path d="M266,92 H284 V70 Q284,58 296,58" fill="none" stroke="var(--gold)" stroke-width="3"/>
    <circle cx="135" cy="92" r="4" fill="var(--gold)"/>
    <circle cx="266" cy="92" r="4" fill="var(--gold)"/>
    <circle cx="168" cy="180" r="4" fill="var(--navy)"/>
    <circle cx="300" cy="180" r="4" fill="var(--navy)"/>
    <circle cx="86" cy="78" r="5" fill="var(--navy)"/><rect x="84" y="83" width="4" height="3" fill="var(--navy)"/>
    <rect x="210" y="74" width="13" height="9" fill="none" stroke="var(--navy)" stroke-width="1.2"/><polyline points="210,74 216.5,79 223,74" fill="none" stroke="var(--navy)" stroke-width="1.2"/>
    <polyline points="343,72 343,85 357,85" fill="none" stroke="var(--navy)" stroke-width="1.4"/><polyline points="345,82 349,77 352,80 357,74" fill="none" stroke="var(--navy)" stroke-width="1.4"/>
  </svg>
  <h2 class="ttl">SECTION TITLE HERE</h2>
  <div class="logo">MEADOWBROOK SCHOOL<br>at LINDEN</div>
  <div class="abs" style="left:46px;top:94px;width:81px"><div class="card-label">ICON HERE</div><p class="p c">Lorem ipsum dolor sit amet, consectetur adipi-scing elit, sed do eius-mod tempor incididunt ut labore et dolore magna aliqua</p></div>
  <div class="abs" style="left:177px;top:94px;width:81px"><div class="card-label">ICON HERE</div><p class="p c">Lorem ipsum dolor sit amet, consectetur adipi-scing elit, sed do eius-mod tempor incididunt ut labore et dolore magna aliqua</p></div>
  <div class="abs" style="left:309px;top:94px;width:81px"><div class="card-label">ICON HERE</div><p class="p c">Lorem ipsum dolor sit amet, consectetur adipi-scing elit, sed do eius-mod tempor incididunt ut labore et dolore magna aliqua</p></div>
  <div class="foot">Copyright text here<span class="pg">Page : 01</span></div>
</section>

<!-- 3 · Donut section -->
<section class="slide" style="left:711px;top:16px">
  <svg class="art" viewBox="0 0 425 240">
    <circle cx="212" cy="114" r="32" fill="none" stroke="var(--navy)" stroke-width="11"/>
    <circle cx="212" cy="114" r="32" fill="none" stroke="var(--red)" stroke-width="11" stroke-dasharray="70 131" transform="rotate(-80 212 114)"/>
    <circle cx="212" cy="114" r="32" fill="none" stroke="#5d6670" stroke-width="11" stroke-dasharray="30 171" transform="rotate(110 212 114)"/>
    <polyline points="140,78 175,78 188,90" fill="none" stroke="#999" stroke-width=".6"/>
    <polyline points="284,78 250,78 238,90" fill="none" stroke="#999" stroke-width=".6"/>
    <polyline points="140,150 175,150 188,138" fill="none" stroke="#999" stroke-width=".6"/>
    <polyline points="284,150 250,150 238,138" fill="none" stroke="#999" stroke-width=".6"/>
  </svg>
  <h2 class="ttl">SECTION <span class="hl">TITLE HERE</span></h2>
  <div class="logo">MEADOWBROOK SCHOOL<br>at LINDEN</div>
  <div class="abs" style="left:12px;top:70px;width:128px"><div class="h red" style="text-align:right">Your Awesome Title One</div><p class="p r">Lorem ipsum dolor sit amet, consectetur adipiscing elit, sed do eiusmod tempor incididunt ut labore et dolore magna aliqua.</p></div>
  <div class="abs" style="left:12px;top:143px;width:128px"><div class="h" style="text-align:right">Your Awesome Title One</div><p class="p r">Lorem ipsum dolor sit amet, consectetur adipiscing elit, sed do eiusmod tempor incididunt ut labore et dolore magna aliqua.</p></div>
  <div class="abs" style="left:286px;top:70px;width:130px"><div class="h red">Your Awesome Title One</div><p class="p">Lorem ipsum dolor sit amet, consectetur adipiscing elit, sed do eiusmod tempor incididunt ut labore et dolore magna aliqua.</p></div>
  <div class="abs" style="left:286px;top:143px;width:130px"><div class="h">Your Awesome Title One</div><p class="p">Lorem ipsum dolor sit amet, consectetur adipiscing elit, sed do eiusmod tempor incididunt ut labore et dolore magna aliqua.</p></div>
  <div class="foot">Copyright text here<span class="pg">Page : 01</span></div>
</section>

<!-- 4 · Numbered rows -->
<section class="slide" style="left:17px;top:213px">
  <svg class="art" viewBox="0 0 425 240">
    <g fill="#fff" stroke="#cfcfcf" stroke-width=".8">
      <rect x="50" y="45" width="342" height="42" rx="4"/><rect x="50" y="102" width="342" height="42" rx="4"/><rect x="50" y="160" width="342" height="42" rx="4"/>
    </g>
    <polygon points="26,66 40,45 54,45 54,87 40,87" fill="var(--navy)"/>
    <polygon points="26,123 40,102 54,102 54,144 40,144" fill="var(--gold)"/>
    <polygon points="26,181 40,160 54,160 54,202 40,202" fill="var(--red)"/>
    <text class="num" x="36" y="69" style="font-size:7px">01</text>
    <text class="num" x="36" y="126" style="font-size:7px">02</text>
    <text class="num" x="36" y="184" style="font-size:7px">03</text>
  </svg>
  <h2 class="ttl">SECTION TITLE HERE</h2>
  <div class="logo">MEADOWBROOK SCHOOL<br>at LINDEN</div>
  <div class="abs row-box" style="left:62px;top:50px;width:320px"><div class="h">Your Awesome Title One</div><p class="p">Lorem ipsum dolor sit amet, consectetur adipiscing elit, sed do eiusmod tempor incididunt ut labore et dolore magna aliqua. Lorem ipsum dolor sit amet, consectetur adipiscing elit, sed do eiusmod tempor incididunt ut labore et dolore magna aliqua. Lorem ipsum dolor sit amet, consectetur adipiscing elit</p></div>
  <div class="abs row-box" style="left:62px;top:107px;width:320px"><div class="h">Your Awesome Title One</div><p class="p">Lorem ipsum dolor sit amet, consectetur adipiscing elit, sed do eiusmod tempor incididunt ut labore et dolore magna aliqua. Lorem ipsum dolor sit amet, consectetur adipiscing elit, sed do eiusmod tempor incididunt ut labore et dolore magna aliqua. Lorem ipsum dolor sit amet, consectetur adipiscing elit</p></div>
  <div class="abs row-box" style="left:62px;top:165px;width:320px"><div class="h">Your Awesome Title One</div><p class="p">Lorem ipsum dolor sit amet, consectetur adipiscing elit, sed do eiusmod tempor incididunt ut labore et dolore magna aliqua. Lorem ipsum dolor sit amet, consectetur adipiscing elit, sed do eiusmod tempor incididunt ut labore et dolore magna aliqua. Lorem ipsum dolor sit amet, consectetur adipiscing elit</p></div>
  <div class="foot">Copyright text here<span class="pg">Page : 01</span></div>
</section>

<!-- 5 · Infographics -->
<section class="slide" style="left:364px;top:213px">
  <svg class="art" viewBox="0 0 425 240">
    <defs><path id="leaf" d="M-2,-2 H-44 A42,42 0 0 1 -86,-44 A42,42 0 0 1 -44,-86 A42,42 0 0 1 -2,-44 Z"/></defs>
    <g transform="translate(313,118)">
      <use href="#leaf" fill="var(--gold)"/>
      <use href="#leaf" fill="var(--navy)" transform="scale(-1,1)"/>
      <use href="#leaf" fill="var(--red)" transform="scale(1,-1)"/>
      <use href="#leaf" fill="var(--gold)" transform="scale(-1,-1)"/>
      <g class="num" text-anchor="middle" style="font-size:10px"><text x="-44" y="-50">01</text><text x="44" y="-50">02</text><text x="-44" y="50">03</text><text x="44" y="50">04</text></g>
    </g>
  </svg>
  <h2 class="ttl">INFOGRAPHICS TITLE HERE</h2>
  <div class="logo">MEADOWBROOK SCHOOL<br>at LINDEN</div>
  <div class="abs" style="left:20px;top:52px;width:170px">
    <div style="font:400 10px var(--serif);color:var(--navy)"><span style="color:var(--gold)">Infographics</span> Title here</div>
    <p class="p j" style="margin-top:6px">Lorem ipsum dolor sit amet, consect eturad eturadi piscing elit, sed do eiusmod tempor incid idunt ut labore Lorem ipsum dolor sit amet, consect eturad ipiscing elit, sed do eiusmod tempor incididunt ut labore lorem ipsum dolor sit amet. Lorem ipsum dolor sit amet, consect eturad eturadi piscing elit, sed do eiusmod tempor incididunt ut labore. Lorem ipsum dolor sit amet, consect eturad piscing elit, sed do e.</p>
    <p class="p j" style="margin-top:5px">Lorem ipsum dolor sit amet, consect eturad eturadi piscing elit, sed do eiusmod tempor incid idunt ut labore Lorem ipsum dolor sit amet, consect eturad ipiscing elit, sed do eiusmod tempor incididunt ut labore lorem ipsum dolor sit amet. Lorem ipsum dolor sit amet, consect eturad piscing elit, sed do eiusmod tempor incididunt ut labore ipsum dolor.</p>
  </div>
  <div class="abs p c" style="left:245px;top:60px;width:50px;color:#fff;font-size:3.2px">Lorem ipsum dolor sit amet, consect eturadi piscing elit, sed do eiusmod</div>
  <div class="abs p c" style="left:331px;top:60px;width:50px;color:#fff;font-size:3.2px">Lorem ipsum dolor sit amet, consect eturadi piscing elit, sed do eiusmod</div>
  <div class="abs p c" style="left:245px;top:140px;width:50px;color:#fff;font-size:3.2px">Lorem ipsum dolor sit amet, consect eturadi piscing elit, sed do eiusmod</div>
  <div class="abs p c" style="left:331px;top:140px;width:50px;color:#fff;font-size:3.2px">Lorem ipsum dolor sit amet, consect eturadi piscing elit, sed do eiusmod</div>
  <div class="foot">Copyright text here<span class="pg">Page : 01</span></div>
</section>

<!-- 6 · Timeline -->
<section class="slide" style="left:711px;top:213px">
  <svg class="art" viewBox="0 0 425 240">
    <rect x="14" y="78" width="99" height="24" fill="var(--navy)"/>
    <rect x="113" y="78" width="99" height="24" fill="var(--gold)"/>
    <rect x="212" y="78" width="100" height="24" fill="var(--green)"/>
    <path d="M312,78 H400 A12,12 0 0 1 412,90 V102 H312 Z" fill="var(--red)"/>
    <text class="year" x="52" y="94">2019</text><text class="year" x="152" y="94">2018</text>
    <text class="year" x="251" y="94">2017</text><text class="year" x="352" y="94">2016</text>
  </svg>
  <h2 class="ttl">TIMELINE <span class="hl">SLIDE</span> HERE</h2>
  <div class="logo">MEADOWBROOK SCHOOL<br>at LINDEN</div>
  <div class="abs" style="left:20px;top:110px;width:85px"><div class="h c" style="text-align:center">Timeline title here</div><p class="p c">Lorem ipsum dolor sit amet, consect eturad eturadi piscing elit, sed do eiusmod tempor incid idunt ut labore ipsum dolor sit amet, consect eturadi piscing elit, sed do pissing elit, sed do e sed do</p></div>
  <div class="abs" style="left:119px;top:110px;width:85px"><div class="h gold" style="text-align:center">Timeline title here</div><p class="p c">Lorem ipsum dolor sit amet, consect eturad eturadi piscing elit, sed do eiusmod tempor incid idunt ut labore ipsum dolor sit amet, consect eturadi piscing elit, sed do pissing elit, sed do e sed do</p></div>
  <div class="abs" style="left:219px;top:110px;width:85px"><div class="h" style="text-align:center;color:var(--green)">Timeline title here</div><p class="p c">Lorem ipsum dolor sit amet, consect eturad eturadi piscing elit, sed do eiusmod tempor incid idunt ut labore ipsum dolor sit amet, consect eturadi piscing elit, sed do pissing elit, sed do e sed do</p></div>
  <div class="abs" style="left:320px;top:110px;width:85px"><div class="h red" style="text-align:center">Timeline title here</div><p class="p c">Lorem ipsum dolor sit amet, consect eturad eturadi piscing elit, sed do eiusmod tempor incid idunt ut labore ipsum dolor sit amet, consect eturadi piscing elit, sed do pissing elit, sed do e sed do</p></div>
  <div class="foot">Copyright text here<span class="pg">Page : 01</span></div>
</section>

<!-- 7 · Team -->
<section class="slide" style="left:17px;top:410px">
  <svg class="art" viewBox="0 0 425 240">
    <g fill="var(--grey)" stroke="#fff" stroke-width="3">
      <circle cx="83" cy="88" r="34"/><circle cx="222" cy="88" r="34"/><circle cx="357" cy="88" r="34"/>
    </g>
    <g fill="none" stroke="var(--gold)" stroke-width=".7">
      <circle cx="83" cy="88" r="37"/><circle cx="222" cy="88" r="37"/><circle cx="357" cy="88" r="37"/>
    </g>
  </svg>
  <h2 class="ttl">TEAM SLIDE HERE</h2>
  <div class="logo">MEADOWBROOK SCHOOL<br>at LINDEN</div>
  <div class="abs" style="left:35px;top:138px;width:96px"><div class="h" style="text-align:center;color:var(--grey)">Team Text here</div><p class="p c">Lorem ipsum dolor sit amet, consect eturadi piscing elit, sed do eiusmod tempor incid idunt ut labore Lorem ipsum dolor sit amet.</p></div>
  <div class="abs" style="left:174px;top:138px;width:96px"><div class="h" style="text-align:center;color:var(--grey)">Team Text here</div><p class="p c">Lorem ipsum dolor sit amet, consect eturadi piscing elit, sed do eiusmod tempor incid idunt ut labore Lorem ipsum dolor sit amet.</p></div>
  <div class="abs" style="left:309px;top:138px;width:96px"><div class="h" style="text-align:center;color:var(--grey)">Team Text here</div><p class="p c">Lorem ipsum dolor sit amet, consect eturadi piscing elit, sed do eiusmod tempor incid idunt ut labore Lorem ipsum dolor sit amet.</p></div>
  <div class="foot">Copyright text here<span class="pg">Page : 01</span></div>
</section>

<!-- 8 · Image left -->
<section class="slide" style="left:364px;top:410px">
  <svg class="art" viewBox="0 0 425 240">
    <defs><linearGradient id="g8" x1="0" y1="0" x2="1" y2="1"><stop offset="0" stop-color="#b7a58c"/><stop offset=".6" stop-color="#6b5d55"/><stop offset="1" stop-color="#2d2f3a"/></linearGradient></defs>
    <g role="img" aria-label="Photo of a student in safety goggles during a science experiment"><path d="M0,0 H118 Q170,0 170,60 V240 H0 Z" fill="url(#g8)"/></g>
    <path d="M124,0 Q176,0 176,60 V235" fill="none" stroke="var(--gold)" stroke-width="1"/>
  </svg>
  <div class="logo">MEADOWBROOK SCHOOL<br>at LINDEN</div>
  <div class="abs" style="left:200px;top:42px;width:214px">
    <div style="font:400 13px var(--serif);color:var(--navy)">IMAGE TITLE HERE</div>
    <p class="p j" style="margin-top:6px">Lorem ipsum dolor sit amet, consect eturadi piscing elit, sed do eiusmod tempor incid idunt ut labore Lorem ipsum dolor sit amet, consect eturadi piscing elit, sed do eiusmod tempor incididunt ut labore Lorem ipsum dolor sit amet, consect eturadi piscing elit, sed do eiusmod tempor incid idunt ut labore Lorem ipsum dolor sit amet, consect eturadi piscing elit, sed do eiusmod tempor incididunt ut labore lorem ipsum dolor sit amet.</p>
    <p class="p j" style="margin-top:5px;color:var(--red);font-style:italic">Lorem ipsum dolor sit amet, consect eturadi piscing elit, sed do eiusmod tempor incid idunt ut labore lorem ipsum dolor sit amet, consect eturadi piscing elit, sed do eiusmod tempor incid idunt ut labore lorem ipsum dolor sit amet, consect eturadi piscing elit, sed do eiusmod.</p>
    <p class="p j" style="margin-top:5px">Lorem ipsum dolor sit amet, consect eturadi piscing elit, sed do eiusmod tempor incid idunt ut labore lorem ipsum dolor sit amet.</p>
  </div>
  <div class="foot">Copyright text here<span class="pg">Page : 01</span></div>
</section>

<!-- 9 · Image right -->
<section class="slide" style="left:711px;top:410px">
  <svg class="art" viewBox="0 0 425 240">
    <defs><linearGradient id="g9" x1="0" y1="0" x2="1" y2="1"><stop offset="0" stop-color="#c9c3b8"/><stop offset=".5" stop-color="#5b6a5a"/><stop offset="1" stop-color="#2f3b46"/></linearGradient></defs>
    <g role="img" aria-label="Photo of a student in a classroom"><path d="M425,0 H310 Q258,0 258,55 V240 H425 Z" fill="url(#g9)"/></g>
    <path d="M304,4 Q252,4 252,58 V235" fill="none" stroke="var(--gold)" stroke-width="1"/>
  </svg>
  <div class="logo" style="color:#fff">MEADOWBROOK SCHOOL<br>at LINDEN</div>
  <div class="abs" style="left:20px;top:40px;width:222px">
    <div style="font:400 13px var(--serif);color:var(--navy)">IMAGE TITLE HERE</div>
    <p class="p j" style="margin-top:5px">Lorem ipsum dolor sit amet, consect eturadi piscing elit, sed do eiusmod tempor incid idunt ut labore Lorem ipsum dolor sit amet, consect eturadi piscing elit, sed do eiusmod tempor incididunt ut labore Lorem ipsum dolor sit amet. Lorem ipsum dolor sit amet, consect eturadi piscing elit, sed do eiusmod tempor incid idunt ut labore Lorem ipsum dolor sit amet, consect eturadi piscing elit, sed do eiusmod tempor incididunt ut labore Lorem ipsum dolor sit amet, consect eturadi piscing elit, sed do eiusmod tempor incid idunt ut labore Lorem ipsum dolor sit amet, consect eturadi piscing elit, sed do eiusmod tempor incididunt ut labore lorem ipsum dolor sit amet. Lorem ipsum dolor sit amet, consect eturadi piscing elit, sed do eiusmod tempor incid idunt ut labore Lorem ipsum dolor sit amet, consect eturadi piscing elit, sed do eiusmod tempor incididunt ut labore lorem ipsum dolor sit amet, consect eturadi piscing elit, sed do eiusmod tempor incid idunt ut labore lorem ipsum dolor sit amet, consect eturadi piscing elit, sed do eiusmod tempor incididunt ut labore lorem ipsum dolor.</p>
  </div>
  <div class="foot">Copyright text here<span class="pg">Page : 01</span></div>
</section>

<!-- 10 · Line chart with panel -->
<section class="slide" style="left:17px;top:607px">
  <svg class="art" viewBox="0 0 425 240">
    <rect x="0" y="45" width="172" height="162" fill="var(--navy)"/>
    <g stroke="#ddd" stroke-width=".4">
      <line x1="195" y1="50" x2="415" y2="50"/><line x1="195" y1="72" x2="415" y2="72"/><line x1="195" y1="94" x2="415" y2="94"/><line x1="195" y1="115" x2="415" y2="115"/><line x1="195" y1="137" x2="415" y2="137"/><line x1="195" y1="158" x2="415" y2="158"/><line x1="195" y1="180" x2="415" y2="180" stroke="#999"/>
    </g>
    <g class="axis" text-anchor="end"><text x="190" y="52">6</text><text x="190" y="74">5</text><text x="190" y="96">4</text><text x="190" y="117">3</text><text x="190" y="139">2</text><text x="190" y="160">1</text><text x="190" y="182">0</text></g>
    <polyline points="200,77 254,66 312,88 410,70" fill="none" stroke="var(--red)" stroke-width="1"/>
    <polyline points="200,117 254,136 312,102 410,130" fill="none" stroke="#333" stroke-width=".9"/>
    <polyline points="200,155 278,140 342,157 410,147" fill="none" stroke="#888" stroke-width=".9"/>
    <g fill="var(--red)"><circle cx="254" cy="66" r="1.3"/><circle cx="312" cy="88" r="1.3"/><circle cx="410" cy="70" r="1.3"/></g>
    <g fill="#333"><circle cx="254" cy="136" r="1.3"/><circle cx="312" cy="102" r="1.3"/><circle cx="410" cy="130" r="1.3"/></g>
    <g class="axis" text-anchor="middle"><text x="218" y="191">LOREM 1</text><text x="278" y="191">LOREM 2</text><text x="342" y="191">LOREM 3</text><text x="398" y="191">LOREM 4</text></g>
    <line x1="253" y1="201" x2="263" y2="201" stroke="#888"/><text class="tiny" x="265" y="202.5">Serie 1</text>
    <line x1="284" y1="201" x2="294" y2="201" stroke="var(--red)"/><text class="tiny" x="296" y="202.5">Serie 2</text>
    <line x1="315" y1="201" x2="325" y2="201" stroke="#333"/><text class="tiny" x="327" y="202.5">Serie 3</text>
  </svg>
  <h2 class="ttl">GRAPHICS TITLE HERE</h2>
  <div class="abs" style="left:10px;top:55px;width:152px"><div class="h" style="color:#fff">GRAPHS TITLE HERE</div><p class="p j" style="color:#dfe5ec;margin-top:2px">Lorem ipsum dolor sit amet, consect eturad piscing elit, sed do eiusmod tempor incid idunt ut labore Lorem ipsum dolor sit amet, consect eturad piscing elit, sed do eiusmod tempor incid idunt ut labore lorem ipsum dolor sit amet. Lorem ipsum dolor sit amet, consect eturad piscing elit, sed do eiusmod tempor incid idunt ut labore Lorem ipsum dolor sit amet, consect eturad piscing elit, sed do eiusmod tempor incid idunt ut labore lorem ipsum dolor sit amet. Lorem ipsum dolor sit amet, consect eturad piscing elit, sed do eiusmod tempor incid idunt ut labore lorem ipsum dolor sit amet, consect eturad piscing elit, sed do eiusmod tempor incid idunt ut labore lorem ipsum dolor sit ame.</p></div>
  <div class="foot">Copyright text here<span class="pg">Page : 01</span></div>
</section>

<!-- 11 · Line + bar charts -->
<section class="slide" style="left:364px;top:607px">
  <svg class="art" viewBox="0 0 425 240">
    <g stroke="#eee" stroke-width=".5">
      <line x1="18" y1="60" x2="195" y2="60"/><line x1="18" y1="80" x2="195" y2="80"/><line x1="18" y1="100" x2="195" y2="100"/><line x1="18" y1="120" x2="195" y2="120"/><line x1="18" y1="140" x2="195" y2="140"/><line x1="18" y1="160" x2="195" y2="160"/>
      <line x1="40" y1="50" x2="40" y2="165"/><line x1="70" y1="50" x2="70" y2="165"/><line x1="100" y1="50" x2="100" y2="165"/><line x1="130" y1="50" x2="130" y2="165"/><line x1="160" y1="50" x2="160" y2="165"/><line x1="190" y1="50" x2="190" y2="165"/>
    </g>
    <polyline points="18,50 18,165 195,165" fill="none" stroke="#bbb" stroke-width=".6"/>
    <path d="M20,162 C40,110 60,85 100,80 S150,78 160,86 S185,80 190,76" fill="none" stroke="var(--red)" stroke-width="1.2"/>
    <path d="M20,162 C40,120 60,100 100,92 S150,100 170,95 S185,90 190,85" fill="none" stroke="var(--gold)" stroke-width="1.2"/>
    <path d="M20,162 C45,128 60,110 100,100 S150,112 165,100 S185,80 190,70" fill="none" stroke="var(--green)" stroke-width="1.2"/>
    <path d="M20,162 C50,150 80,120 110,125 S140,150 160,110 S185,80 190,66" fill="none" stroke="var(--navy)" stroke-width="1.2"/>
    <rect x="68" y="62" width="32" height="9" fill="var(--gold)"/><text class="tiny" x="72" y="68.5" style="fill:#fff">Title Value</text>
    <g fill="var(--grey-light)"><rect x="234" y="72" width="18" height="100"/><rect x="266" y="72" width="18" height="100"/><rect x="298" y="72" width="18" height="100"/><rect x="330" y="72" width="18" height="100"/><rect x="362" y="72" width="18" height="100"/></g>
    <g fill="var(--red)"><rect x="229" y="112" width="23" height="60"/><rect x="261" y="92" width="23" height="80"/><rect x="293" y="122" width="23" height="50"/><rect x="325" y="132" width="23" height="40"/><rect x="357" y="102" width="23" height="70"/></g>
    <g style="font:700 7px var(--sans);fill:var(--red)" text-anchor="middle"><text x="241" y="66">60%</text><text x="273" y="66">80%</text><text x="305" y="66">50%</text><text x="337" y="66">40%</text><text x="369" y="66">70%</text></g>
  </svg>
  <h2 class="ttl">GRAPHICS TITLE HERE</h2>
  <div class="abs" style="left:15px;top:182px;width:180px"><div class="h" style="font-size:5px">GRAPH TITLE HERE</div><p class="p">Lorem ipsum dolor sit amet, consectetur adipiscing elit, sed do eiusmod tempor incididunt ut labore ipsum dolor sit amet lorem ipsum dolor sit amet.</p></div>
  <div class="abs" style="left:228px;top:182px;width:180px"><div class="h red" style="font-size:5px">GRAPH TITLE HERE</div><p class="p">Lorem ipsum dolor sit amet, consectetur adipiscing elit, sed do eiusmod tempor incididunt ut labore ipsum dolor sit amet lorem ipsum dolor sit amet.</p></div>
  <div class="foot">Copyright text here<span class="pg">Page : 01</span></div>
</section>

<!-- 12 · Two-step cycle -->
<section class="slide" style="left:711px;top:607px">
  <svg class="art" viewBox="0 0 425 240">
    <path d="M212,60 A58,58 0 0 0 212,176 L212,160 A42,42 0 0 1 212,76 Z" fill="var(--navy)"/>
    <path d="M212,60 A58,58 0 0 1 212,176 L212,160 A42,42 0 0 0 212,76 Z" fill="var(--red)"/>
    <polygon points="200,48 222,68 200,88" fill="var(--red)"/>
    <polygon points="224,148 202,168 224,188" fill="var(--navy)"/>
    <path d="M212,80 A38,38 0 0 0 212,156 Z" fill="var(--navy)"/>
    <path d="M212,80 A38,38 0 0 1 212,156 Z" fill="var(--red)"/>
    <circle cx="212" cy="118" r="14" fill="#fff"/>
    <circle cx="212" cy="118" r="6" fill="var(--navy)"/>
    <circle cx="172" cy="99" r="3.5" fill="#fff"/><circle cx="252" cy="99" r="4" fill="#fff"/>
    <circle cx="174" cy="146" r="4" fill="none" stroke="#fff" stroke-width=".8"/><path d="M250,142 V152 M246,149 Q250,154 254,149" stroke="#fff" stroke-width=".9" fill="none"/>
    <text x="212" y="72" text-anchor="middle" style="font:700 5px var(--sans);fill:#fff">Step</text><text x="212" y="80" text-anchor="middle" style="font:700 7px var(--sans);fill:#fff">01</text>
    <text x="212" y="166" text-anchor="middle" style="font:700 5px var(--sans);fill:#fff">Step</text><text x="212" y="174" text-anchor="middle" style="font:700 7px var(--sans);fill:#fff">02</text>
    <circle cx="16" cy="84" r="5" fill="var(--navy)"/><text x="16" y="85.7" text-anchor="middle" style="font:700 3.8px var(--sans);fill:#fff">01</text>
    <circle cx="301" cy="84" r="5" fill="var(--red)"/><text x="301" y="85.7" text-anchor="middle" style="font:700 3.8px var(--sans);fill:#fff">02</text>
  </svg>
  <h2 class="ttl">GRAPHICS TITLE HERE</h2>
  <div class="logo">MEADOWBROOK SCHOOL<br>at LINDEN</div>
  <div class="abs" style="left:26px;top:81px;width:100px"><div class="h">STEP – 01</div><p class="p" style="font-size:3.3px">Lorem ipsum dolor sit amet, consectetur adipiscing elit, sed do eiusmod tempor incididunt ut labore dolore. Lorem ipsum dolor sit amet, consectetur adipiscing elit, sed do eiusmod tempor incididunt ut labore dolore. Lorem ipsum dolor sit amet, consectetur adipiscing elit, sed do eiusmod tempor incididunt ut labore dolore. Lorem ipsum dolor sit amet, consectetur adipiscing elit, sed do eiusmod tempor incididunt ut labore dolore magna aliqua.</p></div>
  <div class="abs" style="left:311px;top:81px;width:105px"><div class="h red">STEP – 02</div><p class="p" style="font-size:3.3px">Lorem ipsum dolor sit amet, consectetur adipiscing elit, sed do eiusmod tempor incididunt ut labore dolore. Lorem ipsum dolor sit amet, consectetur adipiscing elit, sed do eiusmod tempor incididunt ut labore dolore. Lorem ipsum dolor sit amet, consectetur adipiscing elit, sed do eiusmod tempor incididunt ut labore dolore. Lorem ipsum dolor sit amet, consectetur adipiscing elit, sed do eiusmod tempor incididunt ut labore dolore magna aliqua.</p></div>
  <div class="foot">Copyright text here<span class="pg">Page : 01</span></div>
</section>

<!-- 13 · Gantt -->
<section class="slide" style="left:17px;top:804px">
  <svg class="art" viewBox="0 0 425 240">
    <rect x="95" y="50" width="320" height="14" fill="#eee"/>
    <rect x="95" y="64" width="320" height="95" fill="#d4d4d4"/>
    <g stroke="#fff" stroke-width=".6"><line x1="121.7" y1="50" x2="121.7" y2="159"/><line x1="148.3" y1="50" x2="148.3" y2="159"/><line x1="175" y1="50" x2="175" y2="159"/><line x1="201.7" y1="50" x2="201.7" y2="159"/><line x1="228.3" y1="50" x2="228.3" y2="159"/><line x1="255" y1="50" x2="255" y2="159"/><line x1="281.7" y1="50" x2="281.7" y2="159"/><line x1="308.3" y1="50" x2="308.3" y2="159"/><line x1="335" y1="50" x2="335" y2="159"/><line x1="361.7" y1="50" x2="361.7" y2="159"/><line x1="388.3" y1="50" x2="388.3" y2="159"/></g>
    <g class="axis" text-anchor="middle" style="font-size:5px"><text x="108" y="59">JAN</text><text x="135" y="59">FEB</text><text x="162" y="59">MAR</text><text x="188" y="59">APR</text><text x="215" y="59">MAY</text><text x="242" y="59">JUN</text><text x="268" y="59">JUL</text><text x="295" y="59">AUG</text><text x="322" y="59">SEP</text><text x="348" y="59">OCT</text><text x="375" y="59">NOV</text><text x="402" y="59">DEC</text></g>
    <g stroke="#333" stroke-width=".5" stroke-dasharray="1.5 1.5"><line x1="15" y1="80" x2="415" y2="80"/><line x1="15" y1="100" x2="415" y2="100"/><line x1="15" y1="120" x2="415" y2="120"/><line x1="15" y1="140" x2="415" y2="140"/></g>
    <rect x="96" y="66" width="74" height="8" rx="4" fill="var(--navy)"/>
    <rect x="176" y="86" width="120" height="8" rx="4" fill="var(--gold)"/>
    <rect x="283" y="106" width="52" height="8" rx="4" fill="var(--red)"/>
    <rect x="340" y="126" width="75" height="8" rx="4" fill="#bbb"/>
    <g style="font:600 3.6px var(--sans);fill:#fff"><text x="104" y="71.5">01.01 &lt;</text><text x="145" y="71.5">&gt; 01.04</text><text x="185" y="91.5">01.04 &lt;</text><text x="272" y="91.5">&gt; 01.08</text><text x="287" y="111.5">01.08 &lt; &gt; 01.10</text><text x="346" y="131.5">01.10 &lt;</text><text x="390" y="131.5">&gt; 31.12</text></g>
    <circle cx="23" cy="71" r="2.3" fill="none" stroke="var(--navy)" stroke-width=".9"/><line x1="21" y1="73" x2="18" y2="76" stroke="var(--navy)" stroke-width=".9"/>
    <circle cx="23" cy="92" r="2.5" fill="var(--navy)"/>
    <circle cx="23" cy="111" r="2.5" fill="var(--navy)"/>
    <circle cx="23" cy="131" r="2.5" fill="none" stroke="var(--grey)" stroke-width=".8"/>
    <g style="font:400 7px var(--sans)"><text x="31" y="74" fill="var(--navy)">Step 01</text><text x="31" y="94" fill="var(--gold)">Step 02</text><text x="31" y="114" fill="var(--red)">Step 03</text><text x="31" y="134" fill="var(--grey)">Step 04</text></g>
    <circle cx="31" cy="172" r="5" fill="var(--gold)"/><circle cx="167" cy="172" r="5" fill="var(--navy)"/><circle cx="303" cy="172" r="5" fill="var(--red)"/>
    <g style="font:700 3.6px var(--sans);fill:#fff" text-anchor="middle"><text x="31" y="173.4">04</text><text x="167" y="173.4">04</text><text x="303" y="173.4">04</text></g>
  </svg>
  <h2 class="ttl">GRAPHICS TITLE HERE</h2>
  <div class="logo">MEADOWBROOK SCHOOL<br>at LINDEN</div>
  <div class="abs" style="left:40px;top:167px;width:115px"><div class="h gold" style="font-size:3.8px">Track our metrics on a calendar</div><p class="p" style="font-size:3.2px">Dolor sit amet, consectetur adipiscing elit, sed do eiusmod tempor incididunt ut labor aliqua.</p></div>
  <div class="abs" style="left:176px;top:167px;width:115px"><div class="h" style="font-size:3.8px">Track our metrics on a calendar</div><p class="p" style="font-size:3.2px">Dolor sit amet, consectetur adipiscing elit, sed do eiusmod tempor incididunt ut labor aliqua.</p></div>
  <div class="abs" style="left:312px;top:167px;width:105px"><div class="h red" style="font-size:3.8px">Track our metrics on a calendar</div><p class="p" style="font-size:3.2px">Dolor sit amet, consectetur adipiscing elit, sed do eiusmod tempor incididunt ut labor aliqua.</p></div>
  <div class="foot">Copyright text here<span class="pg">Page : 01</span></div>
</section>

<!-- 14 · Options columns -->
<section class="slide" style="left:364px;top:804px">
  <svg class="art" viewBox="0 0 425 240">
    <g><polygon points="24,61 29,58 34,61 34,67 29,70 24,67" fill="var(--gold)"/><polygon points="24,96 29,93 34,96 34,102 29,105 24,102" fill="var(--navy)"/><polygon points="24,129 29,126 34,129 34,135 29,138 24,135" fill="var(--red)"/><polygon points="24,164 29,161 34,164 34,170 29,173 24,170" fill="var(--navy)"/></g>
    <g style="font:700 3.5px var(--sans);fill:#fff" text-anchor="middle"><text x="29" y="65.3">01</text><text x="29" y="100.3">02</text><text x="29" y="133.3">03</text><text x="29" y="168.3">04</text></g>
    <polygon points="207,95 231,80 255,95 255,220 207,220" fill="var(--navy)"/>
    <polygon points="260,120 284,105 308,120 308,220 260,220" fill="var(--orange)"/>
    <polygon points="313,95 337,80 361,95 361,220 313,220" fill="var(--gold)"/>
    <polygon points="366,85 390,70 414,85 414,220 366,220" fill="#5f6368"/>
    <g fill="none" stroke-width="3.5" stroke-dasharray="2 1">
      <circle cx="231" cy="62" r="10" stroke="var(--navy)"/><circle cx="284" cy="92" r="10" stroke="var(--orange)"/><circle cx="337" cy="66" r="10" stroke="var(--gold)"/><circle cx="390" cy="52" r="10" stroke="#5f6368"/>
    </g>
    <g style="font:700 6px var(--sans)" text-anchor="middle"><text x="231" y="64" fill="var(--navy)">75%</text><text x="284" y="94" fill="var(--orange)">25%</text><text x="337" y="68" fill="var(--gold)">65%</text><text x="390" y="54" fill="#5f6368">85%</text></g>
    <g style="font:600 4.4px var(--sans);fill:#fff" text-anchor="middle"><text x="231" y="184">Option A</text><text x="284" y="184">Option B</text><text x="337" y="184">Option C</text><text x="390" y="184">Option D</text></g>
    <g stroke="#fff" stroke-width=".6"><line x1="221" y1="188" x2="241" y2="188"/><line x1="274" y1="188" x2="294" y2="188"/><line x1="327" y1="188" x2="347" y2="188"/><line x1="380" y1="188" x2="400" y2="188"/></g>
    <g fill="none" stroke="#fff" stroke-width=".9"><circle cx="231" cy="200" r="3"/><path d="M284,196 V205 M280,202 Q284,207 288,202"/><rect x="333" y="197" width="8" height="6"/><circle cx="390" cy="200" r="4"/></g>
  </svg>
  <h2 class="ttl">GRAPHICS TITLE HERE</h2>
  <div class="logo">MEADOWBROOK SCHOOL<br>at LINDEN</div>
  <div class="abs" style="left:40px;top:58px;width:125px"><div class="h" style="font-size:4px">Break out large tasks into smaller pieces</div><p class="p" style="font-size:3.2px">Dolor sit amet, consectetur adipiscing elit, sed do eiusmod tempor incididunt ut labor aliqua.</p></div>
  <div class="abs" style="left:40px;top:93px;width:125px"><div class="h" style="font-size:4px">Set daily quotas and start every day at zero</div><p class="p" style="font-size:3.2px">Dolor sit amet, consectetur adipiscing elit, sed do eiusmod tempor incididunt ut labor aliqua.</p></div>
  <div class="abs" style="left:40px;top:126px;width:125px"><div class="h" style="font-size:4px">Using app to track progress on specific goals</div><p class="p" style="font-size:3.2px">Dolor sit amet, consectetur adipiscing elit, sed do eiusmod tempor incididunt ut labor aliqua.</p></div>
  <div class="abs" style="left:40px;top:161px;width:125px"><div class="h" style="font-size:4px">Track our metrics on a calendar</div><p class="p" style="font-size:3.2px">Dolor sit amet, consectetur adipiscing elit, sed do eiusmod tempor incididunt ut labor aliqua.</p></div>
  <div class="abs p c" style="left:210px;top:140px;width:42px;color:#fff;font-size:3.2px">Duis tortor, suscipit eget, imperdiet nec, imperdiet</div>
  <div class="abs p c" style="left:263px;top:140px;width:42px;color:#fff;font-size:3.2px">Duis tortor, suscipit eget, imperdiet nec, imperdiet</div>
  <div class="abs p c" style="left:316px;top:140px;width:42px;color:#fff;font-size:3.2px">Duis tortor, suscipit eget, imperdiet nec, imperdiet</div>
  <div class="abs p c" style="left:369px;top:140px;width:42px;color:#fff;font-size:3.2px">Duis tortor, suscipit eget, imperdiet nec, imperdiet</div>
  <div class="foot">Copyright text here<span class="pg">Page : 01</span></div>
</section>

<!-- 15 · Radial arcs -->
<section class="slide" style="left:711px;top:804px">
  <svg class="art" viewBox="0 0 425 240">
    <circle cx="118" cy="132" r="72" fill="none" stroke="#ddd" stroke-width=".6"/>
    <circle cx="118" cy="132" r="62" fill="none" stroke="var(--navy)" stroke-width="3.5" stroke-dasharray="292 400" transform="rotate(-90 118 132)"/>
    <circle cx="118" cy="132" r="54" fill="none" stroke="var(--orange)" stroke-width="3.5" stroke-dasharray="255 400" transform="rotate(-90 118 132)"/>
    <circle cx="118" cy="132" r="46" fill="none" stroke="var(--gold)" stroke-width="3.5" stroke-dasharray="217 400" transform="rotate(-90 118 132)"/>
    <circle cx="118" cy="132" r="38" fill="none" stroke="#666" stroke-width="3.5" stroke-dasharray="179 400" transform="rotate(-90 118 132)"/>
    <circle cx="118" cy="132" r="30" fill="none" stroke="#bbb" stroke-width="3.5" stroke-dasharray="141 400" transform="rotate(-90 118 132)"/>
    <line x1="118" y1="60" x2="118" y2="132" stroke="#ccc" stroke-width=".6"/>
    <circle cx="42" cy="136" r="3" fill="var(--navy)"/><circle cx="60" cy="92" r="2" fill="#999"/><circle cx="118" cy="205" r="2.5" fill="var(--orange)"/>
    <g><polygon points="212,61 217,58 222,61 222,67 217,70 212,67" fill="var(--gold)"/><polygon points="212,98 217,95 222,98 222,104 217,107 212,104" fill="var(--navy)"/><polygon points="212,131 217,128 222,131 222,137 217,140 212,137" fill="var(--orange)"/><polygon points="212,168 217,165 222,168 222,174 217,177 212,174" fill="var(--navy)"/></g>
    <g style="font:700 3.5px var(--sans);fill:#fff" text-anchor="middle"><text x="217" y="65.3">01</text><text x="217" y="102.3">02</text><text x="217" y="135.3">03</text><text x="217" y="172.3">04</text></g>
  </svg>
  <h2 class="ttl">GRAPHICS TITLE HERE</h2>
  <div class="logo">MEADOWBROOK SCHOOL<br>at LINDEN</div>
  <div class="abs" style="left:229px;top:58px;width:140px"><div class="h" style="font-size:4px">Break out large tasks into smaller pieces</div><p class="p" style="font-size:3.2px">Dolor sit amet, consectetur adipiscing elit, sed do eiusmod tempor incididunt ut labor aliqua.</p></div>
  <div class="abs" style="left:229px;top:95px;width:140px"><div class="h" style="font-size:4px">Set daily quotas and start every day at zero</div><p class="p" style="font-size:3.2px">Dolor sit amet, consectetur adipiscing elit, sed do eiusmod tempor incididunt ut labor aliqua.</p></div>
  <div class="abs" style="left:229px;top:128px;width:140px"><div class="h" style="font-size:4px">Using app to track progress on specific goals</div><p class="p" style="font-size:3.2px">Dolor sit amet, consectetur adipiscing elit, sed do eiusmod tempor incididunt ut labor aliqua.</p></div>
  <div class="abs" style="left:229px;top:165px;width:140px"><div class="h" style="font-size:4px">Track our metrics on a calendar</div><p class="p" style="font-size:3.2px">Dolor sit amet, consectetur adipiscing elit, sed do eiusmod tempor incididunt ut labor aliqua.</p></div>
  <div class="foot">Copyright text here<span class="pg">Page : 01</span></div>
</section>

<!-- 16 · Layered circle -->
<section class="slide" style="left:17px;top:1001px">
  <svg class="art" viewBox="0 0 425 240">
    <defs><clipPath id="orb"><circle cx="218" cy="120" r="82"/></clipPath></defs>
    <g clip-path="url(#orb)">
      <rect x="130" y="30" width="180" height="48" fill="var(--red)"/>
      <rect x="130" y="78" width="180" height="42" fill="var(--navy)"/>
      <rect x="130" y="120" width="180" height="40" fill="var(--gold)"/>
      <rect x="130" y="160" width="180" height="50" fill="#9a9a9a"/>
    </g>
    <g stroke="#fff" stroke-width="1.5"><line x1="130" y1="78" x2="310" y2="78"/><line x1="130" y1="120" x2="310" y2="120"/><line x1="130" y1="160" x2="310" y2="160"/></g>
    <g fill="none" stroke="#fff" stroke-width="1.1"><circle cx="202" cy="58" r="4"/><circle cx="200" cy="98" r="4"/><line x1="197" y1="101" x2="193" y2="105"/><path d="M200,132 V144 M195,140 Q200,146 205,140"/><circle cx="200" cy="185" r="5"/></g>
    <g style="font:700 5.5px var(--sans);fill:#fff"><text x="220" y="58">Step</text><text x="220" y="65">04</text><text x="220" y="99">Step</text><text x="220" y="106">03</text><text x="220" y="139">Step</text><text x="220" y="146">02</text><text x="220" y="183">Step</text><text x="220" y="190">01</text></g>
    <g stroke="var(--navy)" stroke-width=".7" fill="none"><polyline points="302,55 312,45 330,45"/><polyline points="140,100 115,100"/><polyline points="300,150 306,163 330,163"/><polyline points="175,200 140,200"/></g>
    <g fill="#bbb"><rect x="42" y="78" width="10" height="2"/><rect x="42" y="82" width="16" height="2"/><rect x="42" y="86" width="12" height="2"/><rect x="365" y="80" width="10" height="2"/><rect x="365" y="84" width="16" height="2"/><rect x="365" y="88" width="12" height="2"/><rect x="363" y="183" width="10" height="2"/><rect x="363" y="187" width="16" height="2"/><rect x="363" y="191" width="12" height="2"/><rect x="64" y="183" width="10" height="2"/><rect x="64" y="187" width="16" height="2"/><rect x="64" y="191" width="12" height="2"/></g>
    <g style="font:700 5px var(--sans)"><text x="22" y="84" fill="var(--navy)">25%</text><text x="345" y="86" fill="var(--red)">45%</text><text x="345" y="189" fill="var(--gold)">15%</text><text x="45" y="189" fill="#999">35%</text></g>
    <g style="font:700 5px var(--sans)"><text x="333" y="47" fill="var(--red)">Title Four</text><text x="72" y="102" fill="var(--navy)">Title Three</text><text x="333" y="165" fill="var(--gold)">Title Two</text><text x="105" y="202" fill="#999">Title One</text></g>
  </svg>
  <h2 class="ttl">GRAPHICS TITLE HERE</h2>
  <div class="abs p" style="left:332px;top:50px;width:85px;font-size:3.3px">Nam pretium turpis et arcu. Duis arcu tortor, suscipit eget, imperdiet nec, imperdiet iaculis ipsum. Sed aliquam ultrices mauris.</div>
  <div class="abs p c" style="left:15px;top:106px;width:110px;font-size:3.3px">Nam pretium turpis et arcu. Duis arcu tortor, suscipit eget, imperdiet nec, imperdiet iaculis ipsum. Sed aliquam ultrices mauris.</div>
  <div class="abs p" style="left:332px;top:168px;width:85px;font-size:3.3px">Nam pretium turpis et arcu. Duis arcu tortor, suscipit eget, imperdiet nec, imperdiet iaculis ipsum. Sed aliquam ultrices mauris.</div>
  <div class="abs p c" style="left:55px;top:205px;width:100px;font-size:3.3px">Nam pretium turpis et arcu. Duis arcu tortor, suscipit eget, imperdiet nec, imperdiet iaculis ipsum.</div>
  <div class="foot">Copyright text here<span class="pg">Page : 01</span></div>
</section>

<!-- 17 · Agenda table -->
<section class="slide" style="left:364px;top:1001px">
  <h2 class="ttl">OUR COURSE AGENDA TABLE</h2>
  <div class="logo">MEADOWBROOK SCHOOL<br>at LINDEN</div>
  <table class="table">
    <colgroup><col style="width:130px"><col style="width:90px"><col style="width:86px"><col style="width:119px"></colgroup>
    <thead><tr><th>Table Title here</th><th>Table Title here</th><th>Table Title here</th><th>Table Title here</th></tr></thead>
    <tbody>
      <tr><td>Paragraph Text Here</td><td>Paragraph Text Here</td><td>Paragraph Text Here</td><td>Paragraph Text Here</td></tr>
      <tr><td>Paragraph Text Here</td><td>Paragraph Text Here</td><td>Paragraph Text Here</td><td>Paragraph Text Here</td></tr>
      <tr><td>Paragraph Text Here</td><td>Paragraph Text Here</td><td>Paragraph Text Here</td><td>Paragraph Text Here</td></tr>
      <tr><td>Paragraph Text Here</td><td>Paragraph Text Here</td><td>Paragraph Text Here</td><td>Paragraph Text Here</td></tr>
      <tr><td>Paragraph Text Here</td><td>Paragraph Text Here</td><td>Paragraph Text Here</td><td>Paragraph Text Here</td></tr>
      <tr><td>Paragraph Text Here</td><td>Paragraph Text Here</td><td>Paragraph Text Here</td><td>Paragraph Text Here</td></tr>
      <tr><td>Paragraph Text Here</td><td>Paragraph Text Here</td><td>Paragraph Text Here</td><td>Paragraph Text Here</td></tr>
      <tr><td>Paragraph Text Here</td><td>Paragraph Text Here</td><td>Paragraph Text Here</td><td>Paragraph Text Here</td></tr>
      <tr><td>Paragraph Text Here</td><td>Paragraph Text Here</td><td>Paragraph Text Here</td><td>Paragraph Text Here</td></tr>
      <tr><td>Paragraph Text Here</td><td>Paragraph Text Here</td><td>Paragraph Text Here</td><td>Paragraph Text Here</td></tr>
      <tr><td>Paragraph Text Here</td><td>Paragraph Text Here</td><td>Paragraph Text Here</td><td>Paragraph Text Here</td></tr>
      <tr><td>Paragraph Text Here</td><td>Paragraph Text Here</td><td>Paragraph Text Here</td><td>Paragraph Text Here</td></tr>
      <tr><td>Paragraph Text Here</td><td>Paragraph Text Here</td><td>Paragraph Text Here</td><td>Paragraph Text Here</td></tr>
      <tr><td>Paragraph Text Here</td><td>Paragraph Text Here</td><td>Paragraph Text Here</td><td>Paragraph Text Here</td></tr>
    </tbody>
  </table>
  <div class="foot">Copyright text here<span class="pg">Page : 01</span></div>
</section>

<!-- 18 · Thank you -->
<section class="slide" style="left:711px;top:1001px;background:var(--navy)">
  <svg class="art" viewBox="0 0 425 240">
    <defs><linearGradient id="g18" x1="0" y1="0" x2="1" y2="1"><stop offset="0" stop-color="#6f7d5e"/><stop offset=".5" stop-color="#9a7b62"/><stop offset="1" stop-color="#3a3530"/></linearGradient></defs>
    <g role="img" aria-label="Photo of two smiling students outdoors"><polygon points="195,240 238,0 425,0 425,240" fill="url(#g18)"/></g>
    <polygon points="187,240 230,0 236,0 193,240" fill="var(--red)"/>
  </svg>
  <div class="thanks">THANK YOU</div>
  <div class="thanks-brand">MEADOWBROOK SCHOOL<br>at LINDEN</div>
  <div class="thanks-addr">120 ORCHARD LANE<br>LINDEN, PA 19000<br>555-014-2290</div>
</section>

</body>
</html>
```